Bright Meadow Counseling Business Card design with a visually interesting use of Space

I need business cards that are luxurious and give a peaceful, calm vibe. I also had some letterhead designed, and i like the look of it also, it's attached with the logo design for reference/ ideas but feel free to be creative.

Target Market(s)

High end luxurious client who needs counseling

Industry/Entity Type

Marriage and Family Therapy

Contact Information for Business Card

Mira Kowalczyk MS LMFT/ or Toby Hallett address 4150 Larkin Suite 600

Font styles to use
Sans Serif

Colors
0054AA
0677BA
7BADD7
CADEEF
E8F1F8
0094D4
00A9DD
6FCCEA
C7EBF8
E9F6FB
A7469A
B969AE
D3A5CF
EDDBEB
F8F0F9
6B429C
8869AF
B7A5CE
E3DAEB
F3F0F8

Requirements
Must have
• Logo and color scheme but be simple modern and luxurious
Nice to have
• I'd like to incorporate some elelmets from the logo and letterhead into a simple modern card

```html
<!DOCTYPE html>
<html lang="en">
<head>
<meta charset="utf-8">
<title>Bright Meadow Counseling – Business Card</title>
<link href="https://fonts.googleapis.com/css2?family=Outfit:wght@200;300;400;500;700&display=swap" rel="stylesheet">
<style>
  :root {
    --backdrop: #e4e4e2;
    --paper: #ffffff;
    --ink: #1c1c1c;
    --plum: #8a4a9c;
    --berry: #a63a78;
    --teal: #3bb0b8;
    --teal-light: #36b1b9;
    --teal-deep: #2d7d8b;
    --mark-violet: #8869af;
    --white: #ffffff;
  }
  * { margin: 0; padding: 0; box-sizing: border-box; }
  html, body {
    width: 1200px; height: 846px; overflow: hidden;
    background: var(--backdrop);
    font-family: "Outfit", sans-serif;
  }
  .card {
    position: absolute; left: 346px; width: 508px; height: 290px;
    overflow: hidden;
  }
  .card--front { top: 99px; background: var(--paper); color: var(--ink); }
  .card--back {
    top: 456px;
    background: radial-gradient(ellipse at 48% 50%, var(--teal-light) 0%, #2f99a6 55%, var(--teal-deep) 100%);
    color: var(--white);
  }

  /* Front */
  .brand { position: absolute; left: 28px; top: 76px; color: var(--ink); font-weight: 200; text-align: right; }
  .brand__name { display: block; font-size: 40px; line-height: 44px; letter-spacing: 0.2px; }
  .brand__sub { display: block; font-size: 18px; line-height: 20px; letter-spacing: 3px; margin-top: 2px; }
  .brand__dot { position: absolute; left: 236px; top: 26px; }

  .person { position: absolute; left: 28px; top: 178px; font-size: 20px; line-height: 24px; }
  .person__name { color: var(--plum); font-weight: 700; }
  .person__creds { color: var(--ink); font-weight: 400; font-size: 16px; }

  .rule { position: absolute; left: 28px; top: 211px; width: 452px; height: 3px; display: flex; gap: 2px; }
  .rule span { flex: 1; }
  .rule .r1 { background: var(--plum); }
  .rule .r2, .rule .r3 { background: var(--berry); }
  .rule .r4 { background: var(--teal); }

  .contact { position: absolute; left: 28px; top: 226px; font-size: 16px; line-height: 20px; font-weight: 300; }
  .contact li { list-style: none; display: flex; align-items: center; gap: 6px; }
  .contact svg { width: 17px; height: 17px; flex: none; }
  .address { position: absolute; right: 28px; top: 226px; text-align: right; font-size: 16px; line-height: 20px; font-weight: 300; }

  /* Back */
  .back__mark { position: absolute; left: 350px; top: 46px; }
  .back__name { position: absolute; left: 46px; top: 132px; font-size: 62px; font-weight: 200; line-height: 70px; letter-spacing: 0.5px; }
  .back__web { position: absolute; left: 61px; top: 206px; font-size: 14px; font-weight: 500; letter-spacing: 1.6px; }
</style>
</head>
<body>

<section class="card card--front">
  <div class="brand">
    <span class="brand__name">Bright Meadow</span>
    <span class="brand__sub">Counseling</span>
  </div>
  <svg class="brand__dot" width="56" height="56" viewBox="0 0 56 56" aria-hidden="true">
    <circle cx="28" cy="28" r="26" fill="var(--mark-violet)" opacity="0.85"/>
  </svg>

  <p class="person"><span class="person__name">Mira Kowalczyk</span> <span class="person__creds">MS LMFT</span></p>

  <div class="rule"><span class="r1"></span><span class="r2"></span><span class="r3"></span><span class="r4"></span></div>

  <ul class="contact">
    <li>
      <svg viewBox="0 0 17 17" aria-hidden="true"><rect x="4" y="0.8" width="9" height="15.4" rx="1.5" fill="none" stroke="var(--teal)" stroke-width="1.6"/><circle cx="8.5" cy="13.4" r="0.9" fill="var(--teal)"/></svg>
      <span>214 555 0148</span>
    </li>
    <li>
      <svg viewBox="0 0 17 17" aria-hidden="true"><rect x="0.5" y="3" width="16" height="11" rx="1" fill="var(--teal)"/><path d="M1 4l7.5 5.5L16 4" fill="none" stroke="var(--white)" stroke-width="1.2"/></svg>
      <span>mira@brightmeadowcounseling.com</span>
    </li>
  </ul>

  <address class="address" style="font-style:normal">4150 Larkin Ave<br>Fairview, TX 75301</address>
</section>

<section class="card card--back">
  <svg class="back__mark" width="110" height="110" viewBox="0 0 110 110" aria-hidden="true">
    <circle cx="55" cy="55" r="50" fill="var(--white)" opacity="0.75"/>
  </svg>
  <p class="back__name">Bright Meadow</p>
  <p class="back__web">WWW.BRIGHTMEADOWCOUNSELING.COM</p>
</section>

</body>
</html>
```